Dorsey K. Wendell Business Card

We need a business card for our company Dorsey K. Wendell Heating & Plumbing to be distributed to potential customers. It should follow the color scheme of our logo and have a modern upscale and masculine look.

The logo is attached and the info below should also be included:

5187 W. Cedar Brook Rd.
Brookvale, PA 17632

Russell T. Wendell
(717) 592-0817
russelltwendell@fernmail.net
dorseykwendell.net
PA #093148

Industry/Entity Type

Business

Contact Information for Business Card

5187 W. Cedar Brook Rd.
Brookvale, PA 17632

Russell T. Wendell
(717) 592-0817
russelltwendell@fernmail.net
dorseykwendell.net
PA #093148

Colors

Designer to choose colors to be used in the design.

Requirements
Must have
• Information above included

```html
<!DOCTYPE html>
<html lang="en">
<head>
<meta charset="utf-8">
<title>Dorsey K. Wendell Business Card</title>
<link rel="stylesheet" href="https://fonts.googleapis.com/css2?family=Open+Sans:wght@400;600;700&display=swap">
<style>
  :root {
    --backdrop: #3b3c3e;
    --card: #1d1e20;
    --blue: #0b87d9;
    --green: #8cc63f;
    --white: #f2f2f2;
  }
  * { margin: 0; padding: 0; box-sizing: border-box; }
  html, body { width: 799px; height: 1200px; overflow: hidden; }
  body {
    background: var(--backdrop);
    font-family: "Open Sans", sans-serif;
    color: var(--white);
    position: relative;
  }
  .card {
    position: absolute;
    left: 60px;
    width: 680px;
    height: 389px;
    background: var(--card);
    border-radius: 4px;
    box-shadow: 0 10px 30px rgba(0,0,0,0.45);
  }
  .card--front { top: 130px; }
  .card--back { top: 680px; }

  .brand {
    position: absolute;
    display: flex;
    align-items: center;
    gap: 14px;
  }
  .brand__square {
    width: 46px;
    height: 46px;
    background: var(--blue);
    flex: none;
  }
  .brand__name {
    font-weight: 700;
    color: var(--blue);
    text-transform: uppercase;
    line-height: 1.15;
    letter-spacing: 0.5px;
    white-space: nowrap;
  }
  .card--front .brand { left: 130px; top: 142px; }
  .card--front .brand__name { font-size: 27px; }
  .card--front .brand__square { width: 76px; height: 76px; }

  .card--back .brand { right: 36px; top: 36px; }
  .card--back .brand__name { font-size: 18px; }
  .card--back .brand__square { width: 52px; height: 52px; }

  .person { position: absolute; left: 36px; top: 112px; }
  .person__name { font-size: 22px; font-weight: 700; color: var(--blue); line-height: 1.3; }
  .person__title { font-size: 13px; margin-top: 2px; }
  .rule {
    position: absolute;
    height: 1px;
    background: var(--green);
  }
  .rule--name { left: 200px; right: 36px; top: 162px; }
  .rule--license { left: 440px; right: 36px; top: 285px; }

  .contacts { position: absolute; left: 36px; top: 185px; list-style: none; }
  .contacts li {
    display: flex; align-items: center; gap: 10px;
    font-size: 14px; line-height: 1.4; margin-bottom: 5px;
  }
  .contacts svg { width: 12px; height: 12px; fill: var(--green); flex: none; }
  .contacts .accent { color: var(--blue); }

  .license {
    position: absolute; right: 36px; top: 256px;
    font-size: 14px; line-height: 1.4;
  }
  .address {
    position: absolute; right: 36px; top: 300px;
    text-align: right; font-size: 15px; line-height: 1.5;
  }
</style>
</head>
<body>
  <section class="card card--front">
    <div class="brand">
      <span class="brand__square"></span>
      <span class="brand__name">Dorsey K. Wendell<br>Heating &amp; Plumbing</span>
    </div>
  </section>

  <section class="card card--back">
    <div class="brand">
      <span class="brand__square"></span>
      <span class="brand__name">Dorsey K. Wendell<br>Heating &amp; Plumbing</span>
    </div>

    <div class="person">
      <p class="person__name">Russell T. Wendell</p>
      <p class="person__title">Managing Director</p>
    </div>
    <div class="rule rule--name"></div>

    <ul class="contacts">
      <li>
        <svg viewBox="0 0 12 12"><path d="M2 1h3l1 3-1.5 1a7 7 0 0 0 2.5 2.5L8 6l3 1v3c0 .6-.4 1-1 1A9 9 0 0 1 1 2c0-.6.4-1 1-1z"/></svg>
        (717) 592-0817
      </li>
      <li>
        <svg viewBox="0 0 12 12"><path d="M0 2h12v8H0z M1 3l5 4 5-4" stroke="#1d1e20" stroke-width="1"/></svg>
        russelltwendell@fernmail.net
      </li>
      <li>
        <svg viewBox="0 0 12 12"><circle cx="6" cy="6" r="6"/></svg>
        <span>www.<span class="accent">dorseykwendell</span>.net</span>
      </li>
    </ul>

    <p class="license">PA #093148</p>
    <div class="rule rule--license"></div>
    <p class="address">5187 W. Cedar Brook Rd.<br>Brookvale, PA 17632</p>
  </section>
</body>
</html>
```